Brisbane IT support business needs our first business card

Hello we are a Brisbane based Information Technology company providing support and services to small and medium sized businesses. We provide a range of services and solutions.

The business name is Wattlebrook Network Computing Services, or WNCS for short.

I am looking for a business card that looks professional (don't we all want that), but most importantly, it most utilize the colours in the logo attached.

Reason: Launched late, extending so people have enough time to actually submit something.

Target Market(s)

Other business owners seeking our IT services, and also home users.

Industry/Entity Type

Business

Requirements
Must have
• Please only use the blue/orange colours in logo attached

```html
<!DOCTYPE html>
<html lang="en">
<head>
<meta charset="utf-8">
<title>WNCS Business Card</title>
<link href="https://fonts.googleapis.com/css2?family=Fira+Sans:wght@500;600&family=Questrial&display=swap" rel="stylesheet">
<style>
  :root {
    --navy: #064863;
    --orange: #ec7f22;
    --white: #ffffff;
    --backdrop: #e9e4de;
  }
  * { margin: 0; padding: 0; box-sizing: border-box; }
  html, body { width: 1200px; height: 900px; overflow: hidden; }
  body {
    position: relative;
    background: var(--backdrop);
    font-family: "Fira Sans", Arial, sans-serif;
  }
  .card {
    position: absolute;
    left: 351px;
    width: 492px;
    overflow: hidden;
    background: var(--white);
    box-shadow: 0 3px 8px rgba(0,0,0,0.25);
  }
  .card--front { top: 143px; height: 290px; }
  .card--back { top: 465px; height: 273px; }

  /* front */
  .front__panel {
    position: absolute; left: 190px; top: 0; width: 302px; height: 237px;
    background: var(--navy);
  }
  .front__rule { position: absolute; left: 0; top: 237px; width: 100%; height: 5px; background: var(--orange); }
  .front__webband {
    position: absolute; left: 0; top: 242px; width: 100%; height: 28px;
    background: var(--navy);
    color: var(--orange);
    font-family: "Questrial", Arial, sans-serif;
    font-size: 19px; letter-spacing: 5px;
    text-align: center; line-height: 28px;
  }
  .front__footband { position: absolute; left: 0; top: 270px; width: 100%; height: 20px; background: var(--orange); }
  .contact {
    position: absolute; right: 14px; top: 74px;
    text-align: right; color: var(--white); font-weight: 600;
  }
  .contact__name { color: var(--orange); font-size: 25px; line-height: 32px; }
  .contact__line { font-size: 18px; line-height: 28px; }

  /* brand lockup */
  .brand { position: absolute; display: flex; align-items: center; }
  .brand__dot { border-radius: 50%; background: var(--navy); flex: none; }
  .brand__divider { background: #9aa7ad; flex: none; }
  .brand__text { color: var(--orange); font-weight: 600; }
  .brand__short { display: block; line-height: 1; }
  .brand__full { display: block; text-transform: uppercase; line-height: 1.15; }

  .card--front .brand { left: 19px; top: 106px; }
  .card--front .brand__dot { width: 54px; height: 54px; }
  .card--front .brand__divider { width: 1px; height: 42px; margin: 0 8px 0 9px; }
  .card--front .brand__short { font-size: 25px; }
  .card--front .brand__full { font-size: 6.5px; width: 82px; }

  /* back */
  .back__orange { position: absolute; left: 0; top: 0; width: 211px; height: 233px; background: var(--orange); }
  .back__bar { position: absolute; left: 211px; top: 0; width: 20px; height: 233px; background: var(--navy); }
  .back__footband { position: absolute; left: 0; top: 233px; width: 100%; height: 40px; background: var(--navy); }
  .card--back .brand { left: 113px; top: 92px; }
  .card--back .brand__dot { width: 88px; height: 88px; }
  .card--back .brand__divider { width: 1px; height: 58px; margin: 0 14px 0 16px; background: #c9a37f; }
  .card--back .brand__short { font-size: 40px; }
  .card--back .brand__full { font-size: 9px; width: 125px; }
</style>
</head>
<body>
  <section class="card card--front">
    <div class="brand">
      <span class="brand__dot"></span>
      <span class="brand__divider"></span>
      <span class="brand__text">
        <span class="brand__short">WNCS</span>
        <span class="brand__full">Wattlebrook Network Computing Services</span>
      </span>
    </div>
    <div class="front__panel">
      <div class="contact">
        <p class="contact__name">Daniel Hartley</p>
        <p class="contact__line">Managing Director</p>
        <p class="contact__line">Telephone: 555.201.4478</p>
        <p class="contact__line">Email: info@wncs.com</p>
      </div>
    </div>
    <div class="front__rule"></div>
    <div class="front__webband">www.wncs.com</div>
    <div class="front__footband"></div>
  </section>

  <section class="card card--back">
    <div class="back__orange"></div>
    <div class="back__bar"></div>
    <div class="back__footband"></div>
    <div class="brand">
      <span class="brand__dot"></span>
      <span class="brand__divider"></span>
      <span class="brand__text">
        <span class="brand__short">WNCS</span>
        <span class="brand__full">Wattlebrook Network Computing Services</span>
      </span>
    </div>
  </section>
</body>
</html>
```